Swimming Pool Supply Company Business Cards

We need business cards designed for company. These need to be easy to edit so that we can fill in names, titles, and contact info for each person who works here.

Dalton R. Whitfield
Manager of Legal & Finance
K.L. Brisbane, Incorporated

4837 Grenway Avenue
Marlow Heights, PA 19243

E. dalton@klbrisbane-example.com
M. (215) 555-0173
O. (215) 555-0148

Contact Information for Business Card

Looking to upgrade current business cards with graphic that can be edited. Looking for fresh ideas for an age old industry.

Font styles to use
Serif
Sans Serif

Colors

Designer to choose colors to be used in the design.

Requirements
Must have
• Professional, fresh, unique but professional

```html
<!DOCTYPE html>
<html lang="en">
<head>
<meta charset="utf-8">
<title>K.L. Brisbane Business Card</title>
<link rel="stylesheet" href="https://fonts.googleapis.com/css2?family=Roboto:wght@400;700;900&family=Libre+Baskerville&display=swap">
<style>
  :root {
    --teal: #1fbfcb;
    --teal-dark: #17a6b1;
    --ink: #111214;
    --paper: #ffffff;
    --stage: #e9e6e1;
    --muted: #c9cfd2;
    --sans: "Roboto", Arial, sans-serif;
    --serif: "Libre Baskerville", Georgia, serif;
  }
  * { box-sizing: border-box; margin: 0; padding: 0; }
  html, body { width: 1200px; height: 796px; overflow: hidden; }
  body { background: var(--stage); font-family: var(--sans); }
  .canvas {
    width: 1200px; height: 796px;
    display: flex; align-items: center; justify-content: center; gap: 40px;
  }
  .card {
    position: relative; width: 540px; height: 309px; overflow: hidden;
    border-radius: 4px; box-shadow: 0 10px 28px rgba(0,0,0,.18);
  }
  .card-shapes { position: absolute; inset: 0; }

  /* Front */
  .card--front { background: var(--paper); }
  .brand-block {
    position: absolute; top: 26px; left: 0; width: 100%; text-align: center;
  }
  .brand-name {
    font-weight: 900; font-size: 40px; letter-spacing: 1px; color: var(--teal); line-height: 1;
  }
  .brand-tagline {
    margin-top: 4px; font-size: 8.5px; font-weight: 700; color: var(--ink);
  }
  .person { position: absolute; left: 22px; top: 150px; color: var(--paper); }
  .person-name { font-size: 23px; font-weight: 700; line-height: 1; }
  .person-title { font-family: var(--serif); font-size: 8.5px; margin-top: 5px; }
  .contact-list { position: absolute; list-style: none; color: var(--paper); font-size: 14px; }
  .contact-list li { display: flex; align-items: center; gap: 12px; height: 32px; }
  .contact-list svg { width: 16px; height: 16px; flex: none; }
  .contact-list--phones { left: 22px; top: 216px; }
  .contact-list--online { left: 322px; top: 128px; font-size: 11.5px; gap: 8px; }
  .contact-list--online li { gap: 9px; }

  /* Back */
  .card--back { background: var(--ink); text-align: center; color: var(--paper); }
  .back-brand {
    margin-top: 92px; font-weight: 900; font-size: 72px; letter-spacing: 2px;
    color: var(--teal); line-height: 1;
  }
  .back-tagline { margin-top: 22px; font-size: 12.5px; font-weight: 700; }
  .back-website { margin-top: 5px; font-size: 11px; color: var(--muted); }
  .back-website span { color: var(--teal); }
</style>
</head>
<body>
<main class="canvas">

  <section class="card card--front" aria-label="Card front">
    <svg class="card-shapes" viewBox="0 0 540 309" aria-hidden="true">
      <polygon class="accent-band" fill="var(--teal)" points="0,138 288,138 318,100 540,100 540,112 330,112 296,200 0,200"/>
      <polygon class="dark-panel" fill="var(--ink)" points="0,200 296,200 330,112 540,112 540,309 0,309"/>
    </svg>

    <div class="brand-block">
      <p class="brand-name">BRISBANE</p>
      <p class="brand-tagline">Big Enough to Serve You, Small Enough to Care</p>
    </div>

    <div class="person">
      <p class="person-name">Dalton R. Whitfield</p>
      <p class="person-title">Manager of Legal &amp; Finance</p>
    </div>

    <ul class="contact-list contact-list--phones">
      <li>
        <svg viewBox="0 0 24 24" aria-hidden="true"><path fill="var(--teal)" d="M6.6 10.8a15.1 15.1 0 0 0 6.6 6.6l2.2-2.2a1 1 0 0 1 1-.25 11.4 11.4 0 0 0 3.6.57 1 1 0 0 1 1 1V20a1 1 0 0 1-1 1A17 17 0 0 1 3 4a1 1 0 0 1 1-1h3.5a1 1 0 0 1 1 1c0 1.25.2 2.45.57 3.57a1 1 0 0 1-.25 1z"/></svg>
        (215) 555-0148
      </li>
      <li>
        <svg viewBox="0 0 24 24" aria-hidden="true"><rect x="6" y="2" width="12" height="20" rx="2" fill="none" stroke="var(--teal)" stroke-width="2"/><circle cx="12" cy="18" r="1.2" fill="var(--teal)"/></svg>
        (215) 555-0173
      </li>
    </ul>

    <ul class="contact-list contact-list--online">
      <li>
        <svg viewBox="0 0 24 24" aria-hidden="true"><circle cx="12" cy="12" r="4" fill="none" stroke="var(--teal)" stroke-width="2.4"/><path d="M16 8v5.5a2.5 2.5 0 0 0 5 0V12a9 9 0 1 0-3.5 7.1" fill="none" stroke="var(--teal)" stroke-width="2.4"/></svg>
        dalton@klbrisbane-example.com
      </li>
      <li>
        <svg viewBox="0 0 24 24" aria-hidden="true"><circle cx="12" cy="12" r="10" fill="var(--teal)"/><path d="M2 12h20M12 2c3 3 3 17 0 20M12 2c-3 3-3 17 0 20" fill="none" stroke="var(--ink)" stroke-width="1.4"/></svg>
        www.klbrisbane-example.com
      </li>
    </ul>
  </section>

  <section class="card card--back" aria-label="Card back">
    <p class="back-brand">BRISBANE</p>
    <p class="back-tagline">Big Enough to Serve You, Small Enough to Care</p>
    <p class="back-website">www.<span>klbrisbane-example</span>.com</p>
  </section>

</main>
</body>
</html>
```